VANTAGE Conference Retractable Standing Banner

I need a design for a 32X80 in retractable banner for a conference. The full title of the conference is the OMRA QLDWN Symposium for Studies on Lasting Involvement in Design, Informatics, and Science. The short name of the conference is VANTAGE. The conference is an academic research conference on equity, diversity, and inclusion in computing, attended by faculty researchers from universities across the US. <br/><br/>Our website is at http://vantage2020.qldwn-example.org. <br/><br/>We typically use the colors purple and white, but are open to other colors being integrated into the design. I attached some previous (terrible) logos just so that you can get an idea of what information we've felt it is important to convey and the color scheme. I would prefer to have something more impactful/graphic in a design.<br/><br/>We prefer clean designs with geometric shapes, and with graphic interest.

Target Market(s)

academic researchers, professors, computer scientists, social scientists, those interested in diversity, equity, and inclusion

Logo Text

VANTAGE

Font styles to use
Sans Serif

Colors
6b449b
33a6d7

Requirements
Must have
• The logo must have the short name of the conference, which is VANTAGE
Nice to have
• The full name of the conference is:
• OMRA QLDWN Symposium for Studies on Fairness and Lasting Involvement in Design, Informatics, and Science (VANTAGE)
• It would be nice to work something in that either includes the words "research on equity and inclusion in computing" or some graphic that captures that concept.
Should not have
• Please don't use 1's and 0's to represent computing - we want to dispel that stereotype.

```html
<!DOCTYPE html>
<html lang="en">
<head>
<meta charset="utf-8">
<title>VANTAGE Conference Banner</title>
<link rel="stylesheet" href="https://fonts.googleapis.com/css2?family=PT+Sans+Narrow:wght@400;700&display=swap">
<style>
  :root {
    --purple-top: #4e168a;
    --purple-mid: #6414ae;
    --purple-low: #540c9a;
    --purple-night: #2e0a52;
    --ribbon-pale: #b9a4d6;
    --ribbon-deep: #7c56ad;
    --accent-blue: #33a6d7;
    --white: #ffffff;
    --text-soft: #ece6f5;
  }
  html, body {
    margin: 0;
    padding: 0;
    width: 815px;
    height: 1200px;
    overflow: hidden;
    background: var(--purple-night);
  }
  .banner {
    position: relative;
    width: 815px;
    height: 1200px;
    overflow: hidden;
    font-family: "PT Sans Narrow", "Arial Narrow", sans-serif;
    color: var(--white);
  }
  .banner__art {
    position: absolute;
    inset: 0;
    width: 815px;
    height: 1200px;
  }
  .banner__organizer {
    position: absolute;
    left: 49px;
    top: 20px;
    margin: 0;
    font-size: 44px;
    font-weight: 400;
    letter-spacing: 0.5px;
  }
  .banner__title {
    position: absolute;
    left: 42px;
    top: 348px;
    margin: 0;
    font-size: 204px;
    font-weight: 400;
    line-height: 1;
    letter-spacing: -2px;
  }
  .banner__subtitle {
    position: absolute;
    left: 50px;
    top: 526px;
    margin: 0;
    font-size: 62px;
    font-weight: 400;
    line-height: 1;
  }
  .banner__tagline {
    position: absolute;
    left: 50px;
    top: 644px;
    margin: 0;
    font-size: 56px;
    line-height: 61px;
    font-weight: 400;
    color: var(--text-soft);
  }
  .banner__website {
    position: absolute;
    left: 50px;
    top: 1150px;
    margin: 0;
    font-size: 22px;
    line-height: 1;
    font-weight: 400;
    color: var(--text-soft);
  }
  .sponsor {
    position: absolute;
    left: 486px;
    top: 1118px;
    display: flex;
    align-items: center;
    gap: 14px;
  }
  .sponsor__dot {
    width: 48px;
    height: 48px;
    border-radius: 50%;
    background: var(--text-soft);
  }
  .sponsor__name {
    margin: 0;
    font-size: 25px;
    line-height: 24px;
    font-weight: 700;
    color: var(--text-soft);
    letter-spacing: 1px;
  }
</style>
</head>
<body>
<main class="banner">
  <svg class="banner__art" viewBox="0 0 815 1200" xmlns="http://www.w3.org/2000/svg">
    <defs>
      <linearGradient id="bg-fill" x1="0" y1="0" x2="0" y2="1">
        <stop offset="0" stop-color="#4e168a"/>
        <stop offset="0.3" stop-color="#6414ae"/>
        <stop offset="0.7" stop-color="#540c9a"/>
        <stop offset="1" stop-color="#2e0a52"/>
      </linearGradient>
      <linearGradient id="ribbon-area" x1="0" y1="1" x2="1" y2="0">
        <stop offset="0" stop-color="#b9a4d6" stop-opacity="0.75"/>
        <stop offset="1" stop-color="#7c56ad" stop-opacity="0.55"/>
      </linearGradient>
      <linearGradient id="wave-area" x1="0" y1="0" x2="0" y2="1">
        <stop offset="0" stop-color="#33a6d7" stop-opacity="0.14"/>
        <stop offset="1" stop-color="#7a3cc4" stop-opacity="0.08"/>
      </linearGradient>
    </defs>

    <rect class="background" width="815" height="1200" fill="url(#bg-fill)"/>

    <g class="background-dots" fill="#7a2cc4" opacity="0.45">
      <circle cx="288" cy="269" r="18"/>
      <circle cx="543" cy="276" r="20"/>
      <circle cx="28" cy="354" r="25"/>
      <circle cx="432" cy="369" r="9"/>
      <circle cx="350" cy="599" r="22"/>
      <circle cx="500" cy="832" r="22"/>
      <circle cx="683" cy="856" r="25"/>
      <circle cx="411" cy="1038" r="30"/>
    </g>

    <rect class="wave-area" x="20" y="260" width="330" height="840" fill="url(#wave-area)"
      role="img" aria-label="Flowing blue line-wave illustration with faint circuit lines and upward arrows"/>

    <polygon class="ribbon-area ribbon-area--top" points="0,135 100,95 815,20 815,116 420,270 0,235"
      fill="url(#ribbon-area)" role="img" aria-label="Folded lilac ribbon illustration crossing the top"/>

    <polygon class="ribbon-area ribbon-area--bottom" points="0,983 120,1005 815,790 815,965 340,1160 0,1110"
      fill="url(#ribbon-area)" role="img" aria-label="Folded lilac ribbon illustration crossing the bottom"/>
  </svg>

  <p class="banner__organizer">OMRA QLDWN</p>
  <h1 class="banner__title">VANTAGE</h1>
  <p class="banner__subtitle">Conference</p>
  <p class="banner__tagline">studies on fairness &amp;<br>lasting involvement<br>in design, informatics,<br>&amp; science</p>

  <p class="banner__website">vantage2020.qldwn-example.org</p>

  <div class="sponsor">
    <span class="sponsor__dot"></span>
    <p class="sponsor__name">OMRA<br>LOGIC<br>GUILD</p>
  </div>
</main>
</body>
</html>
```